The Quiet Hour Safeguard Handbook

A book cover. The book will be marketed as a promotional item for financial advisors, financial planners, independent insurance agents, bankers, and any professional who views their role as guardian of their clients assets and helping them manage risk.

```html
<!DOCTYPE html>
<html lang="en">
<head>
<meta charset="utf-8">
<title>The Quiet Hour Safeguard Handbook</title>
<link href="https://fonts.googleapis.com/css2?family=Poppins:ital,wght@0,600;0,700;1,600;1,700&family=Montserrat:wght@500;700&display=swap" rel="stylesheet">
<style>
  :root {
    --navy-deep: #0a1a30;
    --navy-top: #051a33;
    --sky-blue: #2f6a97;
    --dawn-gold: #f0b560;
    --hill-dark: #2a2a22;
    --gold: #e2ac48;
    --gold-icon: #b8955a;
    --white: #ffffff;
    --tick-green: #6cb33f;
  }
  * { margin: 0; padding: 0; box-sizing: border-box; }
  html, body { width: 800px; height: 1200px; overflow: hidden; background: var(--navy-deep); }
  .cover { position: relative; width: 800px; height: 1200px; overflow: hidden; }

  .hero-scene {
    position: absolute; left: 0; top: 0; width: 800px; height: 958px;
    background: linear-gradient(180deg,
      var(--navy-top) 0%, #0f3b64 22%, var(--sky-blue) 42%,
      #7d98a8 56%, var(--dawn-gold) 66%, #b07a3c 73%,
      #5a4a34 80%, var(--hill-dark) 100%);
  }

  .rule { position: absolute; left: 0; width: 800px; height: 20px; }
  .rule-top { top: 32px; }
  .rule-bottom { top: 376px; }

  .title {
    position: absolute; top: 62px; left: 0; width: 800px; text-align: center;
    font-family: 'Poppins', sans-serif; font-weight: 700; color: var(--white);
    font-size: 72px; line-height: 75px; letter-spacing: -1.5px;
  }
  .subtitle {
    position: absolute; top: 297px; left: 0; width: 800px; text-align: center;
    font-family: 'Poppins', sans-serif; font-style: italic; font-weight: 600;
    color: var(--gold); font-size: 31px; line-height: 35px; letter-spacing: -0.5px;
  }

  .emblem-area {
    position: absolute; left: 307px; top: 425px; width: 184px; height: 202px;
    background: linear-gradient(135deg, #c79a55 0%, #1a3356 45%, #0b1d38 100%);
  }

  .benefit-band {
    position: absolute; left: 0; top: 958px; width: 800px; height: 242px;
    background: var(--navy-deep); border-top: 1px solid #8a6a36;
  }
  .benefits { position: absolute; top: 16px; left: 0; width: 800px; height: 100px; }
  .benefit {
    position: absolute; top: 0; width: 150px; margin-left: -75px; text-align: center;
  }
  .benefit svg { display: block; margin: 0 auto; width: 62px; height: 62px; }
  .benefit-label {
    margin-top: 14px; font-family: 'Montserrat', sans-serif; font-weight: 700;
    color: var(--white); font-size: 15px; letter-spacing: 0.3px; white-space: nowrap;
  }
  .divider { position: absolute; top: 20px; width: 1px; height: 96px; background: var(--gold-icon); }

  .tagline {
    position: absolute; top: 138px; left: 0; width: 800px; text-align: center;
    font-family: 'Montserrat', sans-serif; font-weight: 500; color: var(--white);
    font-size: 22px; line-height: 29px; letter-spacing: 1.8px;
  }
</style>
</head>
<body>
<div class="cover">
  <div class="hero-scene" role="img" aria-label="Sunset over a mountain valley and lake, a family of four seen from behind holding hands on a rocky overlook"></div>

  <svg class="rule rule-top" viewBox="0 0 800 20">
    <line x1="210" y1="10" x2="372" y2="10" stroke="var(--gold)" stroke-width="1.5"/>
    <line x1="428" y1="10" x2="590" y2="10" stroke="var(--gold)" stroke-width="1.5"/>
    <rect x="392" y="2" width="16" height="16" transform="rotate(45 400 10)" fill="var(--gold)"/>
  </svg>

  <h1 class="title">The Quiet Hour<br>Safeguard<br>Handbook</h1>
  <p class="subtitle">Protect Yourself and Your Family<br>in the AI Age</p>

  <svg class="rule rule-bottom" viewBox="0 0 800 20">
    <line x1="210" y1="10" x2="372" y2="10" stroke="var(--gold)" stroke-width="1.5"/>
    <line x1="428" y1="10" x2="590" y2="10" stroke="var(--gold)" stroke-width="1.5"/>
    <rect x="392" y="2" width="16" height="16" transform="rotate(45 400 10)" fill="var(--gold)"/>
  </svg>

  <div class="emblem-area" role="img" aria-label="Gold-rimmed navy shield emblem with a fingerprint motif"></div>

  <section class="benefit-band">
    <div class="benefits">
      <div class="benefit" style="left:79px">
        <svg viewBox="0 0 64 64" aria-hidden="true">
          <path d="M32 4 C22 9 13 11 6 11 L6 32 C6 46 18 56 32 61 C46 56 58 46 58 32 L58 11 C51 11 42 9 32 4 Z" fill="none" stroke="var(--gold-icon)" stroke-width="4"/>
          <circle cx="32" cy="24" r="5" fill="var(--gold-icon)"/>
          <path d="M24 46 L24 36 Q24 31 29 31 L35 31 Q40 31 40 36 L40 46 Z" fill="var(--gold-icon)"/>
        </svg>
        <div class="benefit-label">PROTECT</div>
      </div>
      <div class="divider" style="left:153px"></div>
      <div class="benefit" style="left:232px">
        <svg viewBox="0 0 64 64" aria-hidden="true">
          <path d="M19 28 L19 19 A13 13 0 0 1 45 19 L45 28" fill="none" stroke="var(--gold-icon)" stroke-width="6"/>
          <rect x="10" y="27" width="44" height="33" rx="4" fill="var(--gold-icon)"/>
          <circle cx="32" cy="40" r="4" fill="var(--navy-deep)"/>
          <rect x="30" y="41" width="4" height="9" fill="var(--navy-deep)"/>
        </svg>
        <div class="benefit-label">SECURE</div>
      </div>
      <div class="divider" style="left:300px"></div>
      <div class="benefit" style="left:386px">
        <svg viewBox="0 0 84 64" style="width:84px" aria-hidden="true">
          <circle cx="16" cy="18" r="8" fill="var(--gold-icon)"/>
          <circle cx="68" cy="18" r="8" fill="var(--gold-icon)"/>
          <path d="M1 42 Q1 30 16 30 Q26 30 28 36 L28 44 Z" fill="var(--gold-icon)"/>
          <path d="M83 42 Q83 30 68 30 Q58 30 56 36 L56 44 Z" fill="var(--gold-icon)"/>
          <circle cx="42" cy="16" r="11" fill="var(--gold-icon)"/>
          <path d="M20 58 Q20 32 42 32 Q64 32 64 58 Z" fill="var(--gold-icon)"/>
        </svg>
        <div class="benefit-label">EMPOWER</div>
      </div>
      <div class="divider" style="left:467px"></div>
      <div class="benefit" style="left:540px">
        <svg viewBox="0 0 64 64" aria-hidden="true" fill="none" stroke="var(--gold-icon)" stroke-width="2.5" stroke-linecap="round">
          <path d="M14 14 A26 26 0 0 1 56 28"/>
          <path d="M8 26 A24 24 0 0 1 20 10"/>
          <path d="M12 40 A20 20 0 1 1 52 34 L52 42"/>
          <path d="M18 48 A14 14 0 1 1 46 34 L46 48"/>
          <path d="M26 54 A8 8 0 0 0 30 44 L30 34 A2 2 0 0 1 34 34 L36 56"/>
          <path d="M40 36 A8 8 0 0 0 24 34 L24 44"/>
        </svg>
        <div class="benefit-label">PREPARE</div>
      </div>
      <div class="divider" style="left:608px"></div>
      <div class="benefit" style="left:694px">
        <svg viewBox="0 0 64 64" aria-hidden="true">
          <circle cx="32" cy="32" r="27" fill="none" stroke="var(--tick-green)" stroke-width="5"/>
          <path d="M19 33 L28 42 L46 22" fill="none" stroke="var(--tick-green)" stroke-width="6" stroke-linecap="round" stroke-linejoin="round"/>
        </svg>
        <div class="benefit-label">PEACE OF MIND</div>
      </div>
    </div>

    <p class="tagline">IT’S BETTER TO HAVE IT<br>AND NOT NEED IT THAN NEED IT<br>AND NOT HAVE IT.</p>
  </section>
</div>
</body>
</html>
```